Dalton Perriwether breaking. Or D. Perriwether breaking

I break in and train horses, any age any bread of horse, for any disaplin. I need a business card that is simple but effective, in the way of looking professional. I would like a horse on my card, preferably a horse without a rider. I also pre train horse, younge horses that need a bit of riding before they go into serious work, and prepare yearlings for sale.

Reason: This is for my boyfriend, and I really want it to be perfect and impressive!

Target Market(s)

Thoroughbred race horse trainers, horse industrie people.

Industry/Entity Type

Business

Contact Information for Business Card

Dalton Perriwether horse breaking, "WOLLOMBEE" Tallowvale, give your horse the right start to any career. dperri@mailzone.com.au, 0481392067. Horse breaking~pre-training~sale preparation

```html
<!DOCTYPE html>
<html lang="en">
<head>
<meta charset="utf-8">
<title>Dalton Perriwether – Horse breaking</title>
<link rel="stylesheet" href="https://fonts.googleapis.com/css2?family=Cabin:wght@400;500&family=Questrial&family=Open+Sans:wght@700&display=swap">
<style>
  :root {
    --sky-top: #a89c8a;
    --sky-mid: #8e8a86;
    --sky-low: #b49466;
    --sunset: #e7a13c;
    --sunset-glow: #f6c766;
    --ground: #1d140c;
    --panel-dark: rgba(8, 8, 8, 0.95);
    --panel-grey: rgba(95, 95, 95, 0.55);
    --strip-light: rgba(235, 228, 215, 0.6);
    --band-dark: rgba(30, 22, 16, 0.55);
    --tagline-ink: #1c1c1c;
    --light-ink: #ffffff;
  }
  html, body {
    margin: 0;
    padding: 0;
    width: 1200px;
    height: 693px;
    overflow: hidden;
    background: #ffffff;
  }
  .business-card {
    position: relative;
    width: 1200px;
    height: 693px;
    overflow: hidden;
    font-family: "Questrial", "Century Gothic", sans-serif;
    color: var(--light-ink);
  }
  .backdrop-photo {
    position: absolute;
    inset: 0;
    background:
      radial-gradient(ellipse 45% 22% at 62% 80%, var(--sunset-glow) 0%, rgba(231,161,60,0.6) 45%, rgba(231,161,60,0) 100%),
      linear-gradient(180deg,
        var(--sky-top) 0%,
        #a0978c 18%,
        var(--sky-mid) 45%,
        var(--sky-low) 66%,
        var(--sunset) 78%,
        #6b4220 87%,
        var(--ground) 94%,
        #0d0905 100%);
  }
  .tagline-band {
    position: absolute;
    left: 0; top: 0;
    width: 100%; height: 121px;
    display: flex;
    align-items: center;
    justify-content: center;
  }
  .tagline {
    margin: 0;
    padding-top: 36px;
    font-family: "Cabin", "Trebuchet MS", sans-serif;
    font-size: 50px;
    font-weight: 400;
    line-height: 1;
    color: var(--tagline-ink);
  }
  .light-strip {
    position: absolute;
    left: 0;
    width: 100%;
    background: var(--strip-light);
  }
  .light-strip--upper { top: 121px; height: 13px; }
  .light-strip--lower { top: 435px; height: 28px; }
  .identity-panel {
    position: absolute;
    left: 0; top: 134px;
    width: 100%; height: 301px;
    background: linear-gradient(90deg, var(--panel-dark) 0%, rgba(40,40,40,0.75) 22%, var(--panel-grey) 55%, rgba(110,110,110,0.35) 100%);
  }
  .owner-name {
    position: absolute;
    left: 51px; top: 36px;
    margin: 0;
    font-size: 60px;
    font-weight: 400;
    line-height: 1;
    white-space: nowrap;
  }
  .owner-role {
    position: absolute;
    left: 51px; top: 110px;
    margin: 0;
    font-size: 38px;
    font-weight: 400;
    line-height: 1;
  }
  .contact-list {
    position: absolute;
    right: 52px; top: 141px;
    margin: 0;
    padding: 0;
    list-style: none;
    text-align: right;
    font-size: 36px;
    line-height: 48px;
    white-space: nowrap;
  }
  .contact-list li {
    display: flex;
    justify-content: flex-end;
    align-items: center;
    gap: 8px;
  }
  .contact-icon {
    width: 28px;
    height: 34px;
    fill: none;
    stroke: var(--light-ink);
    stroke-width: 2;
  }
  .services-band {
    position: absolute;
    left: 0; top: 463px;
    width: 100%; height: 85px;
    background: var(--band-dark);
    display: flex;
    align-items: center;
    justify-content: center;
  }
  .services {
    margin: 0;
    font-family: "Open Sans", "Segoe UI", sans-serif;
    font-weight: 700;
    font-size: 47px;
    line-height: 1;
    letter-spacing: -0.3px;
    white-space: nowrap;
  }
</style>
</head>
<body>
  <div class="business-card">
    <div class="backdrop-photo" role="img" aria-label="Photograph of horses galloping in silhouette across a field at sunset under a soft cloudy sky"></div>

    <div class="tagline-band">
      <p class="tagline">give your horse the right start to any career</p>
    </div>
    <div class="light-strip light-strip--upper"></div>

    <section class="identity-panel">
      <h1 class="owner-name">Dalton Perriwether</h1>
      <p class="owner-role">Horse breaking</p>
      <ul class="contact-list">
        <li>“WOLLOMBEE” Tallowvale,</li>
        <li>
          <svg class="contact-icon" viewBox="0 0 28 34" aria-hidden="true">
            <rect x="3" y="9" width="13" height="21" rx="6.5"/>
            <line x1="9.5" y1="9" x2="9.5" y2="16"/>
            <path d="M9.5 9 C10 4, 15 3, 18 6 S 24 9, 27 6"/>
          </svg>
          <span>dperri@mailzone.com.au</span>
        </li>
        <li>
          <svg class="contact-icon" viewBox="0 0 28 34" aria-hidden="true">
            <path d="M17 7 C10 8, 8 14, 8 18 C8 23, 11 28, 18 29" stroke-width="3.5" stroke-linecap="round"/>
          </svg>
          <span>0481392067</span>
        </li>
      </ul>
    </section>

    <div class="light-strip light-strip--lower"></div>
    <div class="services-band">
      <p class="services">Horse breaking - Pre-training - Sale preparation</p>
    </div>
  </div>
</body>
</html>
```